Two Day Training Event includes a Dinner/Bowling Party at Larkspur in Troy, MI

I would like a postcard to attract Insurance Agents to an QWT meeting calling it a summit or something like that. Just something to mail to insurance agents telling them about our upcoming event with over 20 carriers. An opportunity to certify face to face with MAPD carriers and see what 2020 has to offer. Prior to OEP OPen Enrollment and AEP Annual Election period we have a number of meetings. Carriers want to come especially if we can get a number of agents. We are going to go to Larkspur a fun bowling alley for dinner, drinks and bowling to network and talk about the upcoming year.

Target Market(s)

Existing and new insurance agents

Industry/Entity Type

Insurance Broker

Contact Information for Business Card

Looking for a new card design I sent my LOGO and can upload my existing card.

Font styles to use
Serif

Colors

Designer to choose colors to be used in the design.

Requirements
Must have
• Dates Sept 16 and 17th
• location Harrowgate Conference Hall in Troy MI
• times
Nice to have
• It would be nice to see a fun design.

```html
<!DOCTYPE html>
<html lang="en">
<head>
<meta charset="UTF-8">
<title>QWT Training Event Postcard</title>
<link rel="stylesheet" href="https://fonts.googleapis.com/css2?family=Noto+Sans:wght@400;700&family=Archivo:wght@800&display=swap">
<style>
  :root {
    --backdrop: #5ec3ec;
    --panel-navy: #0b2a86;
    --panel-edge: #b9bcc4;
    --card-white: #ffffff;
    --heading-navy: #0e1f63;
    --body-blue: #1a3d8f;
    --invite-teal: #17476e;
    --ornament-blue: #2a4ba3;
  }
  * { margin: 0; padding: 0; box-sizing: border-box; }
  html, body {
    width: 1200px; height: 800px; overflow: hidden;
    background: var(--backdrop);
  }
  .postcard {
    position: absolute; left: 331px; top: 20px;
    width: 537px; height: 760px;
    background: var(--card-white);
    font-family: "Noto Sans", sans-serif;
    overflow: hidden;
  }
  .side-panel {
    position: absolute; left: 0; top: 0;
    width: 168px; height: 100%;
    background: linear-gradient(180deg, #0c2d8c 0%, #09287f 100%);
    border-right: 3px solid var(--panel-edge);
  }
  .corner-ornament { position: absolute; width: 96px; height: 104px; }
  .corner-ornament--top {
    right: 0; top: 0;
    background: radial-gradient(circle at 100% 0%, rgba(42,75,163,0.85) 0%, rgba(42,75,163,0.45) 45%, rgba(42,75,163,0) 72%);
  }
  .corner-ornament--bottom {
    right: 0; bottom: 0;
    background: radial-gradient(circle at 100% 100%, rgba(42,75,163,0.85) 0%, rgba(42,75,163,0.45) 45%, rgba(42,75,163,0) 72%);
  }
  .content { position: absolute; left: 221px; top: 0; right: 0; height: 100%; }
  .content > * { position: absolute; left: 0; white-space: nowrap; }

  .brand { top: 28px; display: flex; align-items: flex-end; gap: 10px; color: var(--ornament-blue); font-weight: 700; }
  .brand-mark { font-size: 40px; line-height: 1; }
  .brand-name { font-size: 12px; line-height: 1.2; padding-bottom: 4px; }

  .invite { top: 96px; font-size: 20px; font-weight: 700; color: var(--invite-teal); line-height: 1.15; }
  .section-title { font-size: 19px; font-weight: 700; color: var(--heading-navy); }
  .event-title { top: 173px; }
  .speakers-title { top: 282px; }
  .venue-title { top: 520px; }
  .contact-title { top: 632px; }

  .detail { font-size: 16px; color: var(--body-blue); }
  .detail--medical { top: 209px; }
  .detail--mapd { top: 242px; }

  .speaker-name { font-size: 17px; color: var(--body-blue); letter-spacing: 1.2px; }
  .speaker-role { font-size: 9.5px; color: var(--body-blue); letter-spacing: 0.3px; }
  .speaker-one { top: 314px; }
  .speaker-one-role { top: 337px; }
  .speaker-two { top: 360px; }
  .speaker-two-role { top: 384px; }

  .connector { top: 424px; left: 114px; font-family: "Archivo", sans-serif; font-weight: 800; font-size: 25px; color: var(--heading-navy); }
  .party { top: 469px; font-family: "Archivo", sans-serif; font-weight: 800; font-size: 16px; letter-spacing: 1.6px; color: var(--heading-navy); }

  .info { font-size: 13px; color: var(--body-blue); letter-spacing: 0.7px; }
  .venue-hall { top: 550px; }
  .venue-place { top: 569px; }
  .venue-date { top: 588px; }
  .venue-time { top: 607px; }
  .contact-street { top: 662px; }
  .contact-city { top: 680px; }
  .contact-phone { top: 702px; }
  .contact-email { top: 721px; }
</style>
</head>
<body>
  <main class="postcard">
    <div class="side-panel" role="img" aria-label="Navy panel with a tone-on-tone floral swirl pattern"></div>
    <div class="corner-ornament corner-ornament--top" role="img" aria-label="Blue floral corner ornament"></div>
    <div class="corner-ornament corner-ornament--bottom" role="img" aria-label="Blue floral corner ornament"></div>

    <section class="content">
      <div class="brand">
        <span class="brand-mark">QWT</span>
        <span class="brand-name">Quorum<br>Wellness Trust</span>
      </div>

      <p class="invite">Inviting you to come<br>and join ---</p>

      <h2 class="section-title event-title">2 Days Training Event :</h2>
      <p class="detail detail--medical">Major medical &amp; senior products</p>
      <p class="detail detail--mapd">Face to face with MAPD carriers</p>

      <h2 class="section-title speakers-title">Speakers :</h2>
      <p class="speaker-name speaker-one">Miles Ardent</p>
      <p class="speaker-role speaker-one-role">(Health and Medicare Specialist)</p>
      <p class="speaker-name speaker-two">Reed Halloway</p>
      <p class="speaker-role speaker-two-role">(Health and Medicare Area Manager)</p>

      <p class="connector">AND</p>
      <p class="party">A DINNER/BOWLING PARTY</p>

      <h2 class="section-title venue-title">Venue &amp; Time :</h2>
      <p class="info venue-hall">HARROWGATE CONFERENCE HALL</p>
      <p class="info venue-place">LARKSPUR IN TROY, MI</p>
      <p class="info venue-date">SEPT 16 &amp; 17</p>
      <p class="info venue-time">03:00 PM - 08:30 PM</p>

      <h2 class="section-title contact-title">Contact Us :</h2>
      <p class="info contact-street">4180 Birchline Ave. Suite 310</p>
      <p class="info contact-city">Troy, MI</p>
      <p class="info contact-phone">(231) 555-0172</p>
      <p class="info contact-email">rhalloway@qwtplans.com</p>
    </section>
  </main>
</body>
</html>
```